Education Foundation Needs a Flyer for an Awareness/Fundraising Event

We need a flyer design for our Education Celebration that is held each year to commemorate Lone Star Learning Days.

This event provides an excellent opportunity for the community to come together to celebrate the education of our children and support the Brookmere Unified Learning District. All twelve schools in the district will have tabletop displays highlighting some of their activities during the year. Teachers will also have grant displays to spotlight the innovative classroom projects they implemented due to funding provided by the Brookmere Learning Trust.

The evening will also include entertainment provided by BULD school choirs. The event concludes with drawing for prices, and a raffle drawing.

Listed below are the details that need to be included in the flyer. I have also included our logo that must be used. I also included some photos from past celebrations that may or may not be helpful.

Please join the Brookmere Learning Trust as we celebrate BULD and its students, educational programs, and schools.

Thursday, March 26, 2015
5:00 p.m. – 8:00 p.m.
Brookmere Senior Academy

Students: Please sign up to be entered in a drawing for Pixora Mini.
Adults: Please sign up to be entered in a drawing for a $50 Shopwell Gift Card.

Raffle Prizes
KORVAN 50" Class 1080p LED Smart HDTV
Zentra Prime Console w/ Motionbar
Donations of $2 each or 3 for $5, or 7 for $10
*Tickets are available at the BULD Administration Building/ Communications and at the schools. (You must be present to win.)

Prizes Galore!
• Campus with the highest percentage of adult attendance will win $300 + the Traveling
Trophy for one year.
• Campus with the 2nd highest percentage of adult attendance will win $150.
• Additional drawings for Teacher, Principal/ Asst. Principal, and District Personnel will be held.

Your Choice – Your Prize
Drawings

7" Dravik NEBULA Pad 4
Fennix Streamlet
Brewlo Classic B20 Single Serve
External Hard Drive
Brewlo 3.0 B700 Coffee Brewing System w/ Carafe
Fennix Streamlet
Cotton Candy Maker
*For your donation of $1.00 per ticket, you may place your ticket(s) in one or all of the baskets. It’s your choice. (You must be present to win.)

Food!
Hot Dogs $1.00
Corn Dogs $0.75
Chips $0.50
Drinks $0.75
Cookies $0.75
Baskets - $2.50 (Hot Dog or Corn Dog, Chips, Drink, Cookie)

For more information, please call 555-318-2946.

```html
<!DOCTYPE html>
<html lang="en">
<head>
<meta charset="utf-8">
<title>Education Celebration Flyer</title>
<link rel="stylesheet" href="https://fonts.googleapis.com/css2?family=Lilita+One&family=Bowlby+One+SC&family=Ubuntu:wght@400;500;700&display=swap">
<style>
  :root{
    --blue:#1f4c9a;
    --blue-dark:#173c7e;
    --red:#a51f3c;
    --yellow:#f3efae;
    --ink:#2a2a2a;
    --white:#ffffff;
    --bg:#e9e6e1;
  }
  *{box-sizing:border-box;margin:0;padding:0}
  html,body{width:1200px;height:945px;overflow:hidden;background:var(--bg)}
  body{font-family:"Ubuntu",sans-serif;color:var(--ink);position:relative}
  .page{position:absolute;top:82px;width:540px;height:780px;overflow:hidden;box-shadow:0 4px 14px rgba(0,0,0,.18)}
  .page--invite{left:45px}
  .page--prizes{left:615px}
  .photo{position:absolute;inset:0}
  .page--invite .photo{background:linear-gradient(160deg,#dfe6f1 0%,#b9c6dc 40%,#e8ecf3 75%,#f4f6f9 100%)}
  .page--prizes .photo{background:linear-gradient(170deg,#f6f3c6 0%,#e9e49a 35%,#d9d48a 60%,#ece7a6 100%)}
  .abs{position:absolute}

  /* logo */
  .brand{left:194px;top:0;width:135px;height:148px;background:var(--white);border:2px solid #333;border-top:none;border-radius:0 0 10px 10px;display:flex;flex-direction:column;align-items:center;justify-content:center;gap:8px;padding:8px}
  .brand__dot{width:54px;height:54px;border-radius:50%;background:var(--blue)}
  .brand__name{font-weight:700;color:var(--blue);font-size:15px;text-align:center;line-height:1.15}

  .headline{left:48px;top:176px;font-family:"Lilita One",sans-serif;font-size:70px;line-height:1;color:var(--blue);letter-spacing:1px}
  .subhead{left:50px;top:250px;font-weight:700;font-size:19px;color:var(--blue);text-transform:uppercase;letter-spacing:.3px}
  .intro{left:50px;top:280px;font-size:11.5px;color:#333}
  .details{left:0;right:0;top:300px;text-align:center;font-size:20px;line-height:29px;color:#222;font-weight:500}

  .signup{left:32px;width:443px}
  .signup__tab{position:absolute;left:130px;width:190px;top:0;height:26px;background:var(--blue);border:2px solid var(--white);border-radius:6px;color:var(--white);font-size:16px;text-align:center;line-height:22px}
  .signup__bar{position:absolute;left:0;right:0;top:20px;height:44px;background:var(--blue);border-radius:10px;color:var(--white);font-size:14.5px;display:flex;align-items:center;justify-content:center;font-weight:500}
  .signup--students{top:388px}
  .signup--adults{top:448px}

  .red-title{font-family:"Bowlby One SC",sans-serif;color:var(--red);line-height:1}
  .raffle-title{left:0;right:0;top:530px;text-align:center;font-size:44px}
  .prize-label{font-size:11px;font-weight:500;color:#111}
  .prize-label--tv{left:8px;top:606px}
  .prize-label--console{right:12px;top:606px}
  .raffle-band{left:168px;top:622px;width:346px;height:82px;background:var(--blue);color:var(--white);font-size:16px;line-height:24px;padding:9px 0 0 28px;font-weight:500}
  .raffle-band p{width:170px;text-align:center}
  .tv{left:8px;top:622px;width:160px;height:86px;background:linear-gradient(135deg,#d8242e,#9e1220);border:4px solid #222}
  .console{left:372px;top:618px;width:132px;height:92px;background:linear-gradient(180deg,#2d2d2d,#111);border-radius:4px}
  .raffle-note{left:0;right:0;top:728px;text-align:center;font-size:12px;line-height:17px;color:#222}

  /* prizes page */
  .galore-title{left:14px;top:30px;font-size:50px}
  .award{background:var(--blue);color:var(--white);border:2px solid var(--white);border-radius:8px;text-align:center;padding-top:10px}
  .award__lead{font-size:10px;line-height:12px;opacity:.9}
  .award__win{font-family:"Bowlby One SC",sans-serif;font-size:27px;line-height:34px;margin-top:4px}
  .award__extra{font-size:8px}
  .award--first{left:8px;top:95px;width:212px;height:88px}
  .award--second{left:244px;top:84px;width:206px;height:92px}
  .extra-drawings{left:132px;top:212px;width:212px;height:76px;background:var(--blue);color:var(--white);border-radius:8px;font-size:13px;line-height:17px;text-align:center;display:flex;align-items:center;justify-content:center;font-weight:500;padding:0 10px}
  .choice-line{left:6px;top:316px;display:flex;align-items:baseline;gap:6px}
  .choice-line__small{font-family:"Lilita One",sans-serif;font-size:15px;color:#111}
  .choice-line__big{font-size:40px}
  .drawings-box{left:11px;top:372px;width:455px;height:120px;background:var(--blue);color:var(--white);border-radius:8px;text-align:center;padding:10px 12px}
  .drawings-box__list{font-size:12.5px;line-height:16px;font-weight:500}
  .drawings-box__rule{border-top:2px dashed var(--white);margin:8px 8px 6px}
  .drawings-box__note{font-size:9.5px;line-height:13px}
  .food-title{left:0;width:480px;top:502px;text-align:center;font-size:38px}
  .menu{left:30px;top:562px;width:445px;height:160px;background:var(--blue);color:var(--white);border-radius:10px;padding:14px 20px;font-size:13px;font-weight:500;list-style:none}
  .menu__row{display:flex;align-items:baseline;line-height:20.5px}
  .menu__dots{flex:1;border-bottom:2px dotted var(--white);margin:0 2px;transform:translateY(-3px)}
  .menu__combo{font-size:8px;font-weight:400}
  .contact{left:34px;top:740px;font-size:17px;color:#333}
  .contact strong{font-size:21px;color:#111}
</style>
</head>
<body>
  <section class="page page--invite">
    <div class="photo" role="img" aria-label="Faded blue-tinted photo of smiling students and families at a past celebration"></div>

    <div class="abs brand">
      <span class="brand__dot"></span>
      <span class="brand__name">Brookmere Learning Trust</span>
    </div>

    <h1 class="abs headline">PLEASE JOIN</h1>
    <p class="abs subhead">The Brookmere Learning Trust</p>
    <p class="abs intro">as we celebrate BULD and its students, educational programs, and schools.</p>

    <p class="abs details">Thursday, March 26, 2015<br>5:00 p.m. – 8:00 p.m.<br>Brookmere Senior Academy</p>

    <div class="abs signup signup--students">
      <div class="signup__bar">Please sign up to be entered in a drawing for Pixora Mini.</div>
      <div class="signup__tab">Students</div>
    </div>
    <div class="abs signup signup--adults">
      <div class="signup__bar">Please sign up to be entered in a drawing for a $50 Shopwell Gift Card.</div>
      <div class="signup__tab">Adults</div>
    </div>

    <h2 class="abs red-title raffle-title">RAFFLE PRIZES</h2>
    <p class="abs prize-label prize-label--tv">KORVAN 50" Class 1080p LED Smart HDTV</p>
    <p class="abs prize-label prize-label--console">Zentra Prime Console w/ Motionbar</p>
    <div class="abs raffle-band"><p>Donations of $2 each<br>or<br>3 for $5, or 7 for $10</p></div>
    <div class="abs tv" role="img" aria-label="Product photo of a flat-screen smart TV"></div>
    <div class="abs console" role="img" aria-label="Product photo of a game console with controller and motion sensor"></div>
    <p class="abs raffle-note">*Tickets are available at the BULD Administration Building/<br>Communications and at the schools. (You must be present to win.)</p>
  </section>

  <section class="page page--prizes">
    <div class="photo" role="img" aria-label="Yellow-tinted photo of a crowd of students and families at a past celebration"></div>

    <h2 class="abs red-title galore-title">PRIZES GALORE!</h2>

    <div class="abs award award--first">
      <p class="award__lead">Campus with the highest percentage<br>of adult attendance will</p>
      <p class="award__win">WIN $300</p>
      <p class="award__extra">+ the Traveling Trophy for one year.</p>
    </div>
    <div class="abs award award--second">
      <p class="award__lead">Campus with the 2nd highest percentage<br>of adult attendance will</p>
      <p class="award__win">WIN $150</p>
    </div>

    <p class="abs extra-drawings">Additional drawings for Teacher Principal/ Asst. Principal and District Personnel will be held.</p>

    <div class="abs choice-line">
      <span class="choice-line__small">YOUR CHOICE · YOUR PRIZE</span>
      <span class="red-title choice-line__big">DRAWINGS</span>
    </div>

    <div class="abs drawings-box">
      <p class="drawings-box__list">7" Dravik NEBULA Pad 4 · Fennix Streamlet · Brewlo Classic B20 Single Serve<br>External Hard Drive · Brewlo 3.0 B700 Coffee Brewing System w/ Carafe<br>Fennix Streamlet · Cotton Candy Maker</p>
      <div class="drawings-box__rule"></div>
      <p class="drawings-box__note">*For your donation of $1.00 per ticket, you may place your ticket (s)<br>in one or all of the baskets. It's your choice.(You must be present to win.)</p>
    </div>

    <h2 class="abs red-title food-title">FOOD</h2>
    <ul class="abs menu">
      <li class="menu__row"><span>Hot Dogs</span><span class="menu__dots"></span><span>$1.00</span></li>
      <li class="menu__row"><span>Corn Dogs</span><span class="menu__dots"></span><span>$0.75</span></li>
      <li class="menu__row"><span>Chips</span><span class="menu__dots"></span><span>$0.50</span></li>
      <li class="menu__row"><span>Drinks</span><span class="menu__dots"></span><span>$0.75</span></li>
      <li class="menu__row"><span>Cookies</span><span class="menu__dots"></span><span>$0.75</span></li>
      <li class="menu__row"><span>Baskets</span><span class="menu__dots"></span><span class="menu__combo">(Hot Dog or Corn Dog, Chips, Drink, Cookie)</span>&nbsp;<span>$2.50</span></li>
    </ul>

    <p class="abs contact">For more information, please call <strong>555-318-2946</strong></p>
  </section>
</body>
</html>
```